Flyer Design Project

We need a flyer for a monthly event that we will be having. The flyer needs to be editable in either adobe illustrator or photoshop so that we can change the details such as the date if needed... Preferable in vector art.

Name of Event : Sandalmania

Price of Tickets: $15 Tickets- Entry fee ensures a pair of thongs upon leaving, drink specials all night and priority entry.

WHEN- FEB 20th
WHERE- Velvet Loft
DJ: Tessa Harlow
web: www.velvetloftbar.com.au
ph: 9146 3705

Drink specials from 7-9pm
$3 Pots
$4 basics
$4 kelvanos

$1 pizza from 8pm-10pm

FREE PAIR OF THONGS ON DEPARTURE

Drink specials continue throughout the night

Open 7pm-3am
Updates

Hi there,

Just to be clear, a pair of thongs isĀ referringĀ to flip flops or sandals (not underwear)... thanks

Target Market(s)

University Students 18-24 years old

Industry/Entity Type

Apartment

Requirements
Must have
• must have our logo

```html
<!DOCTYPE html>
<html lang="en">
<head>
<meta charset="utf-8">
<title>Sandalmania – Velvet Loft</title>
<link rel="stylesheet" href="https://fonts.googleapis.com/css2?family=Bebas+Neue&family=Oswald:wght@500;700&family=Passion+One&display=swap">
<style>
  :root {
    --night: #141414;
    --ink: #0b0b0b;
    --sky: #7fd8ea;
    --sky-deep: #5cc6dd;
    --sun: #f7d417;
    --gold: #cfa90c;
    --lime: #a8f36a;
    --white: #ffffff;
    --panel: rgba(8, 8, 8, 0.86);
  }
  * { margin: 0; padding: 0; box-sizing: border-box; }
  html, body { width: 850px; height: 1200px; overflow: hidden; background: var(--night); }
  .flyer {
    position: relative; width: 850px; height: 1200px; overflow: hidden;
    background:
      repeating-linear-gradient(45deg, rgba(255,255,255,0.025) 0 2px, transparent 2px 5px),
      var(--night);
    font-family: "Bebas Neue", "Oswald", sans-serif;
    color: var(--white);
  }
  .web-band {
    position: absolute; top: 0; left: 0; width: 850px; height: 68px;
    background: repeating-linear-gradient(90deg, var(--sky) 0 3px, var(--sky-deep) 3px 5px);
    border-bottom: 4px solid var(--sky-deep);
    display: flex; align-items: center; justify-content: center;
  }
  .web-band span {
    font-family: "Oswald", sans-serif; font-weight: 700; font-size: 27px;
    letter-spacing: 1.5px; color: #10303a;
  }
  .venue-name {
    position: absolute; left: 22px; top: 80px;
    display: flex; align-items: center; gap: 18px;
  }
  .venue-name .dot { width: 42px; height: 42px; border-radius: 50%; background: var(--white); }
  .venue-name strong {
    font-family: "Oswald", sans-serif; font-weight: 700; font-size: 108px;
    line-height: 1.1; color: var(--white); letter-spacing: 1px;
  }
  .thongs-art {
    position: absolute; left: 650px; top: 200px; width: 200px; height: 175px;
    border-radius: 18px;
    background: linear-gradient(160deg, #2a2a2a 0%, #e98aa8 30%, #7be08a 55%, #6fd3ea 75%, #f4ea6a 100%);
  }
  .freebie {
    position: absolute; left: 22px; top: 272px;
    font-family: "Passion One", sans-serif; font-size: 37px; letter-spacing: 3px; line-height: 1;
    color: var(--sun);
  }
  .event-title {
    position: absolute; left: 42px; top: 340px;
    font-family: "Bebas Neue", sans-serif; font-weight: 400; font-size: 150px; line-height: 1;
    letter-spacing: 1px; color: var(--white); white-space: nowrap;
    transform: scaleY(1.5); transform-origin: left top;
    text-shadow: 2px 1px 0 var(--ink), 4px 2px 0 var(--sun), 6px 3px 0 var(--sun), 8px 4px 0 var(--ink);
  }
  .date-tag {
    position: absolute; left: 34px; top: 563px; width: 406px; height: 68px;
    background: var(--lime); border: 4px solid var(--white);
    display: flex; align-items: center; gap: 10px; padding-left: 18px;
    color: var(--ink); font-size: 52px; letter-spacing: 1px;
  }
  .ribbon { position: absolute; left: 0; top: 620px; width: 850px; height: 240px; }
  .line-stripes {
    position: absolute; left: 0; top: 770px; width: 850px; height: 410px;
    background: repeating-linear-gradient(90deg, transparent 0 26px, var(--gold) 26px 29px);
    opacity: 0.85;
  }
  .washing-line-art {
    position: absolute; left: 0; top: 880px; width: 850px; height: 300px;
    background: linear-gradient(90deg, #55c24a 0%, #6b1e38 30%, #c0366f 45%, #d9c23a 65%, #1c4c5a 85%, #12303a 100%);
    opacity: 0.75;
  }
  .base-strip { position: absolute; left: 0; top: 1180px; width: 850px; height: 20px; background: var(--ink); }
  .ticket-badge {
    position: absolute; left: 496px; top: 570px; width: 350px; height: 350px;
    border-radius: 50%; background: var(--sun);
    display: flex; align-items: center; justify-content: center;
  }
  .ticket-badge .inner {
    width: 318px; height: 318px; border-radius: 50%; background: var(--gold);
    border: 4px dotted var(--sun);
    display: flex; flex-direction: column; align-items: center; justify-content: center;
    text-align: center; color: var(--ink);
  }
  .ticket-badge .crown { width: 46px; height: 36px; margin-bottom: 4px; }
  .ticket-badge .price {
    font-family: "Oswald", sans-serif; font-weight: 700; font-size: 50px; line-height: 1.05;
    color: var(--white); text-shadow: 3px 3px 0 var(--ink);
  }
  .ticket-badge .fee {
    font-family: "Oswald", sans-serif; font-weight: 700; font-size: 34px; letter-spacing: 6px;
    border-bottom: 3px solid var(--ink); padding: 0 6px 8px; margin-bottom: 8px;
  }
  .ticket-badge .note {
    font-family: "Oswald", sans-serif; font-weight: 500; font-size: 21px; letter-spacing: 3px; line-height: 1.15;
  }
  .info-panel {
    position: absolute; left: 155px; top: 912px; width: 695px; height: 258px;
    background: var(--panel); display: flex; padding: 12px 0 0 22px;
  }
  .info-col.specials { width: 356px; }
  .info-col.venue { border-left: 2px solid var(--white); padding-left: 22px; margin-top: 8px; height: 232px; }
  .dj { font-size: 46px; line-height: 1.1; padding-bottom: 6px; border-bottom: 3px dotted var(--white); margin-bottom: 6px; width: 330px; }
  .specials .small { font-size: 29px; line-height: 1.55; }
  .row { display: flex; gap: 28px; }
  .venue .open { font-size: 50px; line-height: 1.05; }
  .venue .big { font-size: 41px; line-height: 1.2; }
  .venue .small { font-size: 29px; margin-top: 10px; line-height: 1.3; }
</style>
</head>
<body>
<main class="flyer">
  <header class="web-band"><span>WWW.VELVETLOFTBAR.COM.AU</span></header>

  <div class="venue-name"><span class="dot"></span><strong>Velvet Loft</strong></div>

  <div class="thongs-art" role="img" aria-label="Stack of colourful flip-flops: black, pink, green, blue and yellow"></div>

  <p class="freebie">FREE PAIR OF THONGS ON DEPARTURE</p>
  <h1 class="event-title">SANDALMANIA</h1>

  <svg class="ribbon" viewBox="0 0 850 240" aria-hidden="true">
    <defs>
      <pattern id="ribbon-lines" width="6" height="10" patternUnits="userSpaceOnUse">
        <rect width="6" height="10" fill="#7fd8ea"/>
        <rect width="2" height="10" fill="#5cc6dd"/>
      </pattern>
    </defs>
    <polygon points="0,122 850,20 850,112 0,216" fill="url(#ribbon-lines)"/>
    <polygon points="420,170 510,160 500,210" fill="#5cc6dd"/>
  </svg>

  <div class="date-tag">
    <svg width="34" height="34" viewBox="0 0 24 24" aria-hidden="true"><polygon points="12,1 15,9 23,9 16.5,14 19,22 12,17 5,22 7.5,14 1,9 9,9" fill="#0b0b0b"/></svg>
    <span>FEBRUARY 20TH</span>
  </div>

  <div class="line-stripes"></div>
  <div class="washing-line-art" role="img" aria-label="Flip-flops pegged on a washing line in green, maroon, pink, yellow and teal"></div>
  <div class="base-strip"></div>

  <div class="ticket-badge">
    <div class="inner">
      <svg class="crown" viewBox="0 0 46 36" aria-hidden="true"><polygon points="2,10 13,20 23,2 33,20 44,10 40,30 6,30" fill="#0b0b0b"/><rect x="6" y="31" width="34" height="4" fill="#0b0b0b"/></svg>
      <div class="price">$15 TICKETS</div>
      <div class="fee">ENTRY FEE</div>
      <div class="note">ENSURES A PAIR OF<br>THONGS UPON<br>LEAVING</div>
    </div>
  </div>

  <section class="info-panel">
    <div class="info-col specials">
      <div class="dj">DJ: TESSA HARLOW</div>
      <div class="small">DRINK SPECIALS FROM 7-9PM</div>
      <div class="small row"><span>$3 POTS</span><span>$1 PIZZA 8PM-10PM</span></div>
      <div class="small">$4 BASICS</div>
      <div class="small">$4 KELVANOS</div>
    </div>
    <div class="info-col venue">
      <div class="open">OPEN 7PM-3AM</div>
      <div class="big">VELVET LOFT</div>
      <div class="big">PH: 9146 3705</div>
      <div class="small">DRINK SPECIALS ALL NIGHT<br>AND PRIORITY ENTRY</div>
    </div>
  </section>
</main>
</body>
</html>
```